We need a modern Google Slides/ PowerPoint presentation for our business brokerage firm in California. Please see attached design colors for colors and fonts- primary colors: white, blue & yellow. On the cover slide we want our logo to be white on blue background (I do not have our logo in white yet, so you can just leave place for logo.) Please limit the amount of stock photos with people. We will insert "Team" photos ourselves, just leave a place for them. Content is attached. Thank you!

```html
<!DOCTYPE html>
<html lang="en">
<head>
<meta charset="utf-8">
<title>Harbor Business Advisors – Presentation</title>
<link rel="stylesheet" href="https://fonts.googleapis.com/css2?family=Lora:wght@400;500&family=Roboto:wght@400;500;700&display=swap">
<style>
:root{
  --navy:#0c2a56;
  --navy-soft:#1a3a68;
  --yellow:#f7e600;
  --white:#ffffff;
  --ink:#333a44;
  --page:#d3d3d3;
}
*{box-sizing:border-box;margin:0;padding:0}
html,body{width:1200px;height:3834px;overflow:hidden;background:var(--page)}
body{position:relative;font-family:'Roboto',Arial,sans-serif;color:var(--ink)}
.slide{position:absolute;left:122px;width:955px;height:478px;background:var(--white);overflow:hidden;box-shadow:0 2px 6px rgba(0,0,0,.12)}
.abs{position:absolute}
.serif{font-family:'Lora',Georgia,serif;font-weight:400}
.brand{color:var(--white);font-family:'Roboto',Arial,sans-serif;font-weight:500;text-align:center;line-height:1.05}
.brand .name{display:block;font-size:24px;letter-spacing:3px;text-transform:uppercase}
.brand .sub{display:block;font-size:9px;letter-spacing:1.5px;text-transform:uppercase}
.header{position:absolute;left:0;top:0;width:100%;height:80px;background:var(--navy);border-bottom:5px solid var(--yellow)}
.header .brand{position:absolute;left:52px;top:20px;text-align:left}

/* cover */
.cover{top:137px;background:var(--navy)}
.cover .brand{position:absolute;left:0;width:100%;top:40px}
.cover-band{position:absolute;left:0;top:115px;width:100%;height:150px;background:var(--navy-soft);text-align:center;color:var(--white)}
.cover-band h1{font-family:'Lora',Georgia,serif;font-weight:400;font-size:29px;margin-top:16px}
.cover-band p{font-size:13px;line-height:21px;margin-top:12px}
.contact{position:absolute;top:314px;width:200px;text-align:center;color:var(--white);font-size:12px;font-weight:500;line-height:20px}
.contact .icon{width:40px;height:40px;border-radius:50%;background:var(--yellow);margin:0 auto 18px;display:flex;align-items:center;justify-content:center}
.divider{position:absolute;top:308px;width:1px;height:107px;background:rgba(255,255,255,.22)}

/* framework */
.framework{top:753px}
.framework .title{position:absolute;right:52px;top:10px;color:var(--white);font-size:40px}
.intro{position:absolute;top:106px;width:100%;text-align:center;font-size:13px;line-height:21px;color:#333}
.timeline{position:absolute;left:60px;top:300px;width:816px;height:2px;background:var(--navy)}
.step-label{position:absolute;width:120px;text-align:center;font-size:13px;font-weight:500;color:#222;line-height:18px}
.step-icon{position:absolute;width:56px;height:56px;border-radius:50%;background:var(--yellow);border:2px solid var(--navy);display:flex;align-items:center;justify-content:center}
.step-note{position:absolute;width:102px;text-align:center;font-size:7.6px;line-height:10.6px;color:#666}
.tick{position:absolute;width:0;height:0;border-left:6px solid transparent;border-right:6px solid transparent}
.tick.up{border-bottom:8px solid var(--navy);top:292px}
.tick.down{border-top:8px solid var(--navy);top:302px}

/* services */
.services{top:1370px}
.services h2{position:absolute;top:100px;width:100%;text-align:center;color:var(--navy);font-size:42px}
.service{position:absolute;top:168px;width:200px;text-align:center}
.service .tag{display:inline-block;width:162px;height:31px;line-height:31px;background:var(--yellow);color:var(--navy);font-size:12.5px;font-weight:500}
.service .glyph{width:60px;height:58px;background:var(--navy);margin:14px auto 12px;display:flex;align-items:center;justify-content:center}
.service p{font-size:11px;line-height:18px;color:#444}
.closer{position:absolute;top:378px;width:100%;text-align:center;color:var(--navy);font-size:17px;line-height:29px}

/* photo slides */
.photo{position:absolute;left:0;top:85px;width:100%;height:393px}
.upfront{top:1988px}
.upfront .photo{background:linear-gradient(180deg,#e7ecef 0%,#c6d2da 45%,#7e95a6 78%,#5a7184 100%)}
.upfront h2{position:absolute;left:83px;top:150px;color:var(--navy);font-size:40px;line-height:42px;color:#1f2530}
.upfront p{position:absolute;left:83px;top:261px;width:430px;font-size:12.5px;line-height:20.5px;color:#222;text-align:justify}
.planning{top:2604px}
.planning .photo{background:linear-gradient(120deg,#2e7d80 0%,#5f9c9c 40%,#8fa8a2 70%,#a9a996 100%)}
.card{position:absolute;left:454px;top:138px;width:432px;height:247px;background:var(--white);padding:20px 32px}
.card-shadow{position:absolute;left:729px;top:265px;width:165px;height:128px;background:var(--navy)}
.card h2{font-size:40px;line-height:42px;color:#222}
.card p{margin-top:14px;font-size:12.5px;line-height:20.5px;color:#222;text-align:justify}
.tech{top:3220px}
.tech .photo{background:linear-gradient(160deg,#f2f4fb 0%,#e4e9f6 50%,#d6deef 100%)}
.tech-frame{position:absolute;left:164px;top:189px;width:630px;height:167px;background:var(--white);border:2px solid var(--navy);text-align:center;padding-top:16px}
.tech-offset{position:absolute;left:177px;top:179px;width:630px;height:167px;border:2px solid var(--yellow)}
.tech-frame h2{font-size:40px;color:#222}
.tech-frame p{margin-top:14px;font-size:12.5px;line-height:20.5px;color:#222}
</style>
</head>
<body>

<!-- Cover -->
<section class="slide cover">
  <div class="brand"><span class="name">Harbor</span><span class="sub">Business Advisors</span></div>
  <div class="cover-band">
    <h1>We sell businesses more effectively</h1>
    <p>We are a full-service business brokerage &amp; M&amp;A advisory firm in California.<br>With our proven strategic framework, we sell privately held businesses at a<br>greater value and in less time</p>
  </div>
  <div class="contact" style="left:61px">
    <div class="icon"><svg width="16" height="16" viewBox="0 0 16 16"><circle cx="8" cy="5" r="3.2" fill="#0c2a56"/><path d="M2 15c0-4 3-6 6-6s6 2 6 6z" fill="#0c2a56"/></svg></div>
    License Number<br>12345678
  </div>
  <div class="divider" style="left:265px"></div>
  <div class="contact" style="left:273px">
    <div class="icon"><svg width="16" height="18" viewBox="0 0 16 18"><path d="M8 1a5.5 5.5 0 0 0-5.5 5.5C2.5 11 8 17 8 17s5.5-6 5.5-10.5A5.5 5.5 0 0 0 8 1z" fill="#0c2a56"/><circle cx="8" cy="6.5" r="2" fill="#f7e600"/></svg></div>
    Address<br>123,Lorem ipsum dolor sit<br>amet, consectetu
  </div>
  <div class="divider" style="left:476px"></div>
  <div class="contact" style="left:485px">
    <div class="icon"><svg width="16" height="16" viewBox="0 0 16 16"><path d="M3 1.5l3 .5 1 3-1.8 1.3a9 9 0 0 0 4.5 4.5L11 9l3 1 .5 3c-1 1.5-3 1.8-5 .8A14 14 0 0 1 2.2 6.5C1.2 4.5 1.5 2.5 3 1.5z" fill="#0c2a56"/></svg></div>
    Phone<br>+1 888 888 8888
  </div>
  <div class="divider" style="left:688px"></div>
  <div class="contact" style="left:697px">
    <div class="icon"><svg width="16" height="16" viewBox="0 0 16 16"><circle cx="8" cy="8" r="7" fill="#0c2a56"/><path d="M4 6c2 0 2 2 4 2s1 3 3 3M9 2c0 2 2 2 3 4" stroke="#f7e600" stroke-width="1.3" fill="none"/></svg></div>
    Website<br>www.harborba.com
  </div>
</section>

<!-- Framework -->
<section class="slide framework">
  <div class="header"><div class="brand"><span class="name">Harbor</span><span class="sub">Business Advisors</span></div>
    <h2 class="title serif">Our Framework</h2></div>
  <p class="intro">We've helped hundreds of clients to sell their business at higher value by<br>following our strategic framework.</p>
  <div class="timeline"></div>

  <div class="step-label" style="left:53px;top:186px">Preparation &amp;<br>Planning</div>
  <div class="step-icon" style="left:85px;top:225px"><svg width="28" height="24" viewBox="0 0 28 24" fill="none" stroke="#0c2a56" stroke-width="1.6"><rect x="3" y="6" width="22" height="15"/><path d="M7 17v-5M11 17v-7M15 17v-3M19 17v-6"/></svg></div>
  <div class="tick up" style="left:107px"></div>
  <div class="step-note" style="left:62px;top:316px">This phase focuses on preparing your business for sale. We believe that advanced preparation is the key to success. It makes your business more attractive to potential buyers and allows you to get the best price for it.</div>

  <div class="step-note" style="left:208px;top:177px">We will advise you on the best method(s) to use to determine the price range for your business, help you gather the documents and understand the key factors that drive the value of your business. Business valuation</div>
  <div class="tick down" style="left:253px"></div>
  <div class="step-icon" style="left:231px;top:319px"><svg width="26" height="26" viewBox="0 0 26 26" fill="none" stroke="#0c2a56" stroke-width="1.6"><rect x="5" y="3" width="16" height="20"/><circle cx="13" cy="13" r="4"/><path d="M9 7h8"/></svg></div>
  <div class="step-label" style="left:199px;top:380px">Business<br>Valuation</div>

  <div class="step-label" style="left:344px;top:186px">Marketing the<br>Business</div>
  <div class="step-icon" style="left:376px;top:225px"><svg width="26" height="26" viewBox="0 0 26 26" fill="none" stroke="#0c2a56" stroke-width="1.6"><circle cx="13" cy="13" r="9"/><path d="M8 13l4 4 6-8"/></svg></div>
  <div class="tick up" style="left:398px"></div>
  <div class="step-note" style="left:353px;top:316px">Once we've established the price and overall sales strategy, we will prepare a comprehensive marketing plan and begin promoting your business to qualified strategic buyers and business brokers. To maintain confidentiality, your</div>

  <div class="step-note" style="left:498px;top:177px">A non-disclosure agreement must be signed by all interested buyers. Your business will be exposed to a wide range of buyers to generate competitive bids. We only work with buyers who meet the appropriate financial</div>
  <div class="tick down" style="left:543px"></div>
  <div class="step-icon" style="left:521px;top:319px"><svg width="28" height="22" viewBox="0 0 28 22" fill="none" stroke="#0c2a56" stroke-width="1.6"><path d="M2 12l6-6 6 3 6-3 6 6-8 7-6-4"/><circle cx="14" cy="5" r="3"/></svg></div>
  <div class="step-label" style="left:489px;top:380px">Meet the<br>buyer</div>

  <div class="step-label" style="left:634px;top:186px">Offers &amp;<br>Negotiations</div>
  <div class="step-icon" style="left:666px;top:225px"><svg width="28" height="24" viewBox="0 0 28 24" fill="none" stroke="#0c2a56" stroke-width="1.6"><path d="M2 14l6-6 6 3 6-3 6 6-8 7-6-4z"/><path d="M9 4h10"/></svg></div>
  <div class="tick up" style="left:688px"></div>
  <div class="step-note" style="left:643px;top:316px">During this phase of the process, our goal is to produce the best possible offer for your business. We will assist you in evaluating each offer with our expertise on current market trends, financing matters and business</div>

  <div class="step-note" style="left:789px;top:225px">We will work closely with your CPA, landlord, attorney, and all relevant third parties to ensure a smooth closing.</div>
  <div class="tick down" style="left:834px"></div>
  <div class="step-icon" style="left:812px;top:319px"><svg width="26" height="26" viewBox="0 0 26 26" stroke="#0c2a56" stroke-width="3.2" stroke-linecap="round"><path d="M6 6l14 14M20 6L6 20"/></svg></div>
  <div class="step-label" style="left:780px;top:380px">Closing</div>
</section>

<!-- What we do -->
<section class="slide services">
  <div class="header"><div class="brand"><span class="name">Harbor</span><span class="sub">Business Advisors</span></div></div>
  <h2 class="serif">What we do</h2>
  <div class="service" style="left:59px"><span class="tag">EXIT PLANNING</span>
    <div class="glyph"><svg width="34" height="32" viewBox="0 0 34 32" fill="none" stroke="#f7e600" stroke-width="1.5"><rect x="4" y="6" width="20" height="22"/><path d="M8 12h12M8 17h12M8 22h8M22 4l8 8"/></svg></div>
    <p>Exit planning strategy will identify the actions that need to be taken so that you can exit your business with confidence.</p></div>
  <div class="service" style="left:271px"><span class="tag">BUSINESS VALUATIONS</span>
    <div class="glyph"><svg width="34" height="30" viewBox="0 0 34 30" fill="none" stroke="#f7e600" stroke-width="1.5"><rect x="3" y="8" width="28" height="19" rx="2"/><path d="M12 8V4h10v4M3 16h28"/><rect x="15" y="14" width="4" height="5"/></svg></div>
    <p>By utilizing a variety of valuation methods, we will evaluate your business and determine the most probable selling price.</p></div>
  <div class="service" style="left:482px"><span class="tag">SELLER REPRESENT</span>
    <div class="glyph"><svg width="34" height="32" viewBox="0 0 34 32" fill="none" stroke="#f7e600" stroke-width="1.5"><circle cx="11" cy="10" r="6"/><path d="M11 4v6h6M8 28v-6M13 28v-9M18 28v-7M23 28v-11M28 28v-14M20 12l10-8"/></svg></div>
    <p>With our proven strategic framework, we'll help you to sell your business at a greater value and in less time</p></div>
  <div class="service" style="left:695px"><span class="tag">BUYER REPRESENT</span>
    <div class="glyph"><svg width="34" height="32" viewBox="0 0 34 32" fill="none" stroke="#f7e600" stroke-width="1.5"><circle cx="13" cy="11" r="5"/><circle cx="24" cy="7" r="3"/><path d="M3 24l8-2 10 2 10-5M3 28h28"/></svg></div>
    <p>From deal sourcing to closing, we guide business buyers through the entire process to set them up for success.</p></div>
  <p class="closer serif">Talking To Other Business Brokerage Firms? Awesome, we encourage that.<br>But here are a few things that make us different...</p>
</section>

<!-- Upfront costs -->
<section class="slide upfront">
  <div class="header"><div class="brand"><span class="name">Harbor</span><span class="sub">Business Advisors</span></div></div>
  <div class="photo" role="img" aria-label="Photo of a businessman on a pedestal looking through binoculars over a hazy city"></div>
  <h2 class="serif">We don’t charge<br>upfront costs.</h2>
  <p>We are able to deliver world class business brokerage services without upfront costs for our clients. Our fees are success-based. With a success-based pricing model, our commission is earned AFTER the business is sold.</p>
</section>

<!-- Preparation & Planning -->
<section class="slide planning">
  <div class="header"><div class="brand"><span class="name">Harbor</span><span class="sub">Business Advisors</span></div></div>
  <div class="photo" role="img" aria-label="Photo of a hand holding a glowing light bulb surrounded by a network of connected points"></div>
  <div class="card-shadow"></div>
  <div class="card">
    <h2 class="serif">Preparation &amp;<br>Planning</h2>
    <p>Advanced preparation is the key to success. We help you to prepare your business for sale before it goes on the market. Exit planning strategy will make your business more attractive to the potential buyers and allow you to maximize the value of your business.</p>
  </div>
</section>

<!-- Technology -->
<section class="slide tech">
  <div class="header"><div class="brand"><span class="name">Harbor</span><span class="sub">Business Advisors</span></div></div>
  <div class="photo" role="img" aria-label="Faint pale blue background of charts and data graphics"></div>
  <div class="tech-offset"></div>
  <div class="tech-frame">
    <h2 class="serif">Technology Driven Process</h2>
    <p>We have a proven, technology-driven process.  It allows us to effectively manage the sales<br>transaction from every angle and move the deal towards closing faster.</p>
  </div>
</section>

</body>
</html>
```